Buch-/E-Book-Cover für Ernährungsratgeber
Danke für die schöne Idee und das tolle Design! Darauf käme ich gern wieder zurück.
Zielgruppe
Ich bin freiberuflich tätige Autorin. Mit dem neuen Buch möchte ich Frauen von 18-45 ansprechen, die sich für gesunde Ernährung interessieren aber gleichzeitig gern zu Süßigkeiten greifen.
Aufgabenstellung
Der Designer sollte sich an die im PDF-Dokument vorgegebenen Abmessungen halten. Zusätzlich habe ich meinen eigenen Entwurf hochgeladen, an dem man sich orientieren könnte. Denkbar, und wahrscheinlich attraktiver, wäre auch ein einzelner Eyecatcher in der Mitte des Covers, z.B. ein Cupcake mit Teufelshörnern o.ä. Ich bin allerdings genauso offen für ganz neue Ideen! Bitte bringen Sie Titel und Autorin auf dem Cover unter, sowie auf dem schmalen Buchrücken. Den Kurztext auf der Rückseite lassen Sie weg, auch für den Untertitel wird kein Platz gebraucht - er soll wegfallen.
Autorin: Minna Holtrop
Titel: "Mondlicht über dem Zuckerbäcker"
Alternativtitel: "Naschwerk oder Nährwert?"
Der Fokus liegt hier stark auf dem "teuflischen" Element bzw. dem "teuflischen Cupcake". Es soll vermittelt werden, wie verführerisch aber gleichzeitig auch teuflisch/schädlich die süßen Kreationen der Lebensmittelindustrie sind.
Ich freue mich auf Ihre Entwürfe!

```html
<!DOCTYPE html>
<html lang="de">
<head>
<meta charset="utf-8">
<title>Mondlicht über dem Zuckerbäcker – Minna Holtrop</title>
<link rel="stylesheet" href="https://fonts.googleapis.com/css2?family=Arimo:wght@700&family=Cherry+Swash:wght@400;700&display=swap">
<style>
  :root {
    --pink-deep: #e9578b;
    --pink-mid: #f08db0;
    --pink-soft: #f5b4cb;
    --pink-base: #f09ab8;
    --white: #ffffff;
    --frosting: #e98ab6;
    --frosting-light: #f3b3d2;
    --sponge: #f0c27e;
    --wrapper: #f2a88a;
  }
  html, body {
    margin: 0;
    padding: 0;
    overflow: hidden;
    background: var(--pink-soft);
  }
  .cover {
    position: relative;
    width: 777px;
    height: 1200px;
    overflow: hidden;
    background:
      radial-gradient(ellipse 70% 45% at 50% 60%, rgba(255,255,255,0.28), rgba(255,255,255,0) 70%),
      linear-gradient(180deg, var(--pink-deep) 0%, var(--pink-mid) 35%, var(--pink-soft) 70%, var(--pink-base) 100%);
    color: var(--white);
  }
  .author {
    position: absolute;
    top: 62px;
    left: 0;
    width: 100%;
    margin: 0;
    text-align: center;
    font-family: "Arimo", Arial, sans-serif;
    font-weight: 700;
    font-size: 29px;
    letter-spacing: 0.3px;
  }
  .title {
    position: absolute;
    top: 142px;
    left: 40px;
    right: 40px;
    margin: 0;
    text-align: center;
    font-family: "Cherry Swash", Georgia, serif;
    font-weight: 400;
    text-transform: uppercase;
    line-height: 1;
  }
  .title-line {
    display: block;
  }
  .title-line--top {
    font-size: 84px;
    letter-spacing: 1px;
  }
  .title-link {
    font-family: "Arimo", Arial, sans-serif;
    font-weight: 700;
    font-size: 27px;
    letter-spacing: 1px;
    margin: 6px 0 8px;
  }
  .title-line--bottom {
    font-size: 68px;
    letter-spacing: 0;
  }
  .hero {
    position: absolute;
    left: 165px;
    top: 440px;
    width: 607px;
    height: 555px;
  }
</style>
</head>
<body>
  <main class="cover">
    <p class="author">Minna Holtrop</p>
    <h1 class="title">
      <span class="title-line title-line--top">Mondlicht</span>
      <span class="title-line title-link">über dem</span>
      <span class="title-line title-line--bottom">Zuckerbäcker</span>
    </h1>
    <svg class="hero" viewBox="0 0 607 555" role="img" aria-label="Illustration: rosa Cupcake mit roten Teufelshörnern und Teufelsschwanz">
      <defs>
        <linearGradient id="heroFill" x1="0" y1="0" x2="0" y2="1">
          <stop offset="0%" stop-color="var(--frosting-light)"/>
          <stop offset="40%" stop-color="var(--frosting)"/>
          <stop offset="55%" stop-color="var(--sponge)"/>
          <stop offset="100%" stop-color="var(--wrapper)"/>
        </linearGradient>
      </defs>
      <rect x="0" y="0" width="440" height="520" rx="60" fill="url(#heroFill)" opacity="0.85"/>
    </svg>
  </main>
</body>
</html>
```